Flyer for an online formula one racing league

Hello.

I am looking for the perfect one page facebook/instagram style flyer for an online formula one racing league. The racing league is called 'VOLKA RACING LEAGUE'.

Information that MUST be on the new flyer is already on the old flyer I have uploaded here. In addition to including: The Volka racing league 'R' logo I have uploaded AND the text: 'Very popular, clean and competitive racing league, running for its 4th season. Why not join with a friend? Race times, Mondays, Tuesdays and Wednesdays each at 8pm UK TIME Message below for any questions. (Spacing of information is not important, however all the information in regards to the racing I have just mentioned MUST BE on the flyer, this includes info from old pic, logo and the other info I just mentioned).

It would be beneficial to have lots of dark blue on the flyer and the new flyer to be a lot different to the original flyer I uploaded, but this is not essential.

I apologise if I did not explain very well, any questions, please message me.

The best flyer should look the most attractive to someone that might be interested in joining an online formula one racing league.

I used this website before to create the perfect logo for my Sunday League team last year, and I was very impressed. I look forward to seeing your submissions.

Target Market(s)

No specific target, more something that may attract someone into joining a formula one online racing league

Industry/Entity Type

e sports/formula one

Colors
0054AA
0677BA
7BADD7
CADEEF
E8F1F8

Requirements
Must have
• Read product description please
Should not have
• Ignoring product description!

```html
<!DOCTYPE html>
<html lang="en">
<head>
<meta charset="utf-8">
<title>Volka Racing League – New Season</title>
<link rel="stylesheet" href="https://fonts.googleapis.com/css2?family=Montserrat:ital,wght@0,500;0,700;1,800;1,900&family=Russo+One&family=Bungee&display=swap">
<style>
  :root {
    --page-bg: #d4d4d4;
    --navy-deep: #0a0b2e;
    --navy: #14164a;
    --indigo: #2a1f7a;
    --crimson: #d0123e;
    --magenta: #e0207a;
    --blue-bright: #2a6cff;
    --cyan: #19c8ff;
    --white: #ffffff;
    --orange: #ff8a1f;
  }
  * { margin: 0; padding: 0; box-sizing: border-box; }
  html, body { width: 1200px; height: 814px; overflow: hidden; background: var(--page-bg); }
  .flyer {
    position: absolute; left: 0; top: 93px; width: 1200px; height: 628px; overflow: hidden;
    background:
      linear-gradient(180deg, rgba(10,11,46,0) 0%, rgba(10,11,46,0) 60%, rgba(6,10,50,.85) 100%),
      linear-gradient(90deg, var(--navy-deep) 0%, var(--navy) 40%, #1a0f3e 100%);
    font-family: "Montserrat", sans-serif; color: var(--white);
  }
  .streaks { position: absolute; inset: 0; }
  .flag-art {
    position: absolute; right: 0; top: 0; width: 280px; height: 240px;
    background: radial-gradient(ellipse at 70% 40%, rgba(220,200,235,.55), rgba(150,40,150,.35) 50%, rgba(20,15,60,0) 75%);
  }
  .car-art {
    position: absolute; right: 0; bottom: 0; width: 300px; height: 260px;
    background: radial-gradient(ellipse at 60% 50%, rgba(255,150,40,.8), rgba(220,40,40,.55) 40%, rgba(20,30,90,.3) 70%, rgba(20,15,60,0) 85%);
  }
  .gauge-art {
    position: absolute; left: 0; bottom: 0; width: 180px; height: 180px;
    background: radial-gradient(circle at 50% 55%, rgba(255,40,40,.8) 0%, rgba(255,140,40,.5) 25%, rgba(40,160,255,.35) 55%, rgba(10,11,46,0) 75%);
  }
  .brand-badge {
    position: absolute; left: 32px; top: 63px; width: 148px; height: 148px; border-radius: 50%;
    background: var(--navy-deep); border: 4px solid var(--white);
    display: flex; align-items: center; justify-content: center;
  }
  .brand-name { font-family: "Montserrat", sans-serif; font-weight: 700; font-size: 26px; color: var(--white); letter-spacing: 1px; }
  .content { position: absolute; left: 0; top: 0; width: 1200px; text-align: center; }
  .title {
    position: absolute; left: 200px; width: 744px; top: 52px; font-family: "Russo One", sans-serif;
    font-size: 54px; transform: skewX(-12deg); letter-spacing: 1px;
    background: linear-gradient(90deg, var(--magenta), var(--orange) 30%, #ffe81f 50%, #ff6a2a 70%, var(--magenta));
    -webkit-background-clip: text; background-clip: text; color: transparent; white-space: nowrap;
  }
  .subtitle { position: absolute; left: 372px; width: 400px; top: 128px; font-weight: 700; font-size: 30px; white-space: nowrap; }
  .subtitle sup { font-size: 15px; vertical-align: 12px; }
  .season-band {
    position: absolute; left: 259px; top: 182px; width: 680px; height: 58px;
    clip-path: polygon(3% 0, 100% 0, 97% 100%, 0 100%);
    background: linear-gradient(90deg, #ff1f8a, #ff8a1f 30%, #ffe81f 50%, #4cff7a 75%, #19e0ff);
    display: flex; align-items: center; justify-content: center;
  }
  .season-text {
    font-family: "Montserrat", sans-serif; font-weight: 900; font-style: italic; font-size: 33px;
    color: var(--white); -webkit-text-stroke: 1.5px var(--navy-deep); letter-spacing: .5px;
  }
  .pitch { position: absolute; left: 200px; width: 744px; top: 256px; font-weight: 800; font-style: italic; font-size: 26px; line-height: 39px; }
  .days {
    position: absolute; left: 180px; width: 784px; top: 376px; font-family: "Bungee", sans-serif;
    font-size: 42px; line-height: 54px; transform: skewX(-10deg);
    background: linear-gradient(180deg, var(--cyan), var(--blue-bright));
    -webkit-background-clip: text; background-clip: text; color: transparent;
  }
  .details { position: absolute; left: 200px; width: 760px; top: 490px; font-weight: 500; font-size: 18px; line-height: 26.5px; }
  .details sup { font-size: 10px; }
</style>
</head>
<body>
  <main class="flyer">
    <svg class="streaks" width="1200" height="628" viewBox="0 0 1200 628" aria-hidden="true">
      <defs>
        <linearGradient id="streak-blue" x1="0" x2="1"><stop offset="0" stop-color="#3a3cff"/><stop offset="1" stop-color="#3a3cff" stop-opacity="0"/></linearGradient>
        <linearGradient id="streak-red" x1="0" x2="1"><stop offset="0" stop-color="#ff1a3a"/><stop offset=".6" stop-color="#d0123e" stop-opacity=".6"/><stop offset="1" stop-color="#d0123e" stop-opacity="0"/></linearGradient>
      </defs>
      <rect x="0" y="20" width="420" height="10" fill="url(#streak-blue)"/>
      <rect x="0" y="45" width="600" height="22" fill="url(#streak-blue)" opacity=".7"/>
      <rect x="0" y="110" width="380" height="30" fill="url(#streak-blue)" opacity=".8"/>
      <rect x="0" y="180" width="300" height="8" fill="url(#streak-blue)"/>
      <rect x="0" y="255" width="1000" height="34" fill="url(#streak-red)"/>
      <rect x="0" y="300" width="800" height="14" fill="url(#streak-red)" opacity=".7"/>
      <rect x="0" y="330" width="1100" height="40" fill="url(#streak-red)" opacity=".5"/>
      <rect x="0" y="395" width="600" height="10" fill="url(#streak-red)" opacity=".6"/>
    </svg>
    <div class="flag-art" role="img" aria-label="Waving chequered racing flag"></div>
    <div class="car-art" role="img" aria-label="Classic car speeding with orange motion blur"></div>
    <div class="gauge-art" role="img" aria-label="Glowing speedometer dial"></div>

    <div class="brand-badge"><span class="brand-name">VOLKA</span></div>

    <div class="content">
      <h1 class="title">VOLKA RACING LEAGUE</h1>
      <p class="subtitle">RUNNING FOR ITS 4<sup>TH</sup> YEAR</p>
      <div class="season-band"><span class="season-text">NEW SEASON JUST STARTING!!!</span></div>
      <p class="pitch">CLEAN ONLINE RACING LEAGUE<br>3 DIVISIONS CURRENTLY AND LOOKING<br>TO KEEP GROWING!</p>
      <p class="days">Spaces Left On Mondays,<br>Tuesdays And Wednesdays!!!</p>
      <p class="details">Very popular, clean and competitive racing league, running for its 4<sup>th</sup> season.<br>Why not join with a friend? Race times, Mondays, Tuesdays and Wednesdays<br>each at 8pm UK TIME. Message below for any questions.</p>
    </div>
  </main>
</body>
</html>
```